Label Design for honey from a small farm in Italy

We need a label for our Acacia's honey .
We are a little farm in Italy and we would like something like organic, raw and simple.
Maybe with botanical drawing with different color like watercolor o something like that (very important natural and easy)
the jar for 1kg of honey: Capacity: 780 ml - Height: 137 mm - Diameter: ∅ 94 mm
- size approx h 5,5 x 10/14cm ( we use the same label for kg and 500 gr jar)

Industry/Entity Type

Farm

Requirements
Must have
• the writings:
- Acacia
- Miele italiano di Acacia
- Da consumarsi preferibilmente entro: ( and below the space to put the date by the hands)
- some space to put some presentation of the farm or some phrases
- our logo
- the space to put the weight by the hands
- Prodotto da Azienda Agricola ...(produced by Farm Name and address....)
- Confezionato presso Apicoltura... (packaged at apiculture Name and address..)
- graphic of Acacia’s flowers ( like drawing)
Should not have
• Barcode
nutritional table

```html
<!DOCTYPE html>
<html lang="it">
<head>
<meta charset="utf-8">
<title>Acacia – Miele italiano di Acacia</title>
<link rel="stylesheet" href="https://fonts.googleapis.com/css2?family=Stint+Ultra+Condensed&family=Lato:wght@400&display=swap">
<style>
  :root {
    --paper: #ffffff;
    --frame: #d5cab6;
    --divider: #dcd3c4;
    --ink-dark: #4a3f30;
    --ink-gold: #bea98a;
    --ink-brand: #b8a688;
    --art-light: #f7f2e8;
    --art-mid: #eee5d4;
  }
  * { box-sizing: border-box; margin: 0; padding: 0; }
  html, body {
    width: 1200px;
    height: 661px;
    overflow: hidden;
    background: var(--paper);
  }
  .label {
    position: relative;
    width: 1200px;
    height: 661px;
    background: var(--paper);
    font-family: "Lato", Arial, sans-serif;
  }
  .label__frame {
    position: absolute;
    left: 15px;
    top: 13px;
    width: 1151px;
    height: 626px;
    border: 4px solid var(--frame);
    border-radius: 18px;
  }
  .flower-art {
    position: absolute;
    left: 200px;
    top: 100px;
    width: 144px;
    height: 228px;
    border-radius: 40px 60px 50px 50px / 40px 40px 120px 120px;
    background: radial-gradient(ellipse at 55% 45%, var(--art-mid) 0%, var(--art-light) 60%, rgba(247,242,232,0) 100%);
  }
  .product-name {
    position: absolute;
    left: 124px;
    top: 346px;
    width: 340px;
    font-family: "Stint Ultra Condensed", "Arial Narrow", serif;
    font-weight: 400;
    font-size: 148px;
    line-height: 1;
    letter-spacing: 14px;
    color: var(--ink-dark);
    white-space: nowrap;
  }
  .product-subtitle {
    position: absolute;
    left: 127px;
    top: 488px;
    font-size: 21px;
    letter-spacing: 2.3px;
    color: var(--ink-dark);
    white-space: nowrap;
  }
  .label__divider {
    position: absolute;
    left: 589px;
    top: 78px;
    width: 1.5px;
    height: 494px;
    background: var(--divider);
  }
  .brand {
    position: absolute;
    left: 790px;
    top: 112px;
    display: flex;
    align-items: center;
    gap: 10px;
  }
  .brand__mark {
    width: 10px;
    height: 10px;
    background: var(--ink-brand);
  }
  .brand__name {
    font-size: 24px;
    letter-spacing: 1.5px;
    color: var(--ink-brand);
    white-space: nowrap;
  }
  .fields {
    position: absolute;
    left: 699px;
    top: 364px;
    width: 330px;
  }
  .field { height: 73px; }
  .field__label {
    font-size: 13.5px;
    letter-spacing: 1.3px;
    color: var(--ink-gold);
    white-space: nowrap;
    line-height: 16px;
  }
  .field__line {
    margin-top: 29px;
    height: 2px;
    width: 330px;
    background-image: radial-gradient(circle, var(--ink-gold) 0.9px, transparent 1.2px);
    background-size: 9.2px 2px;
    background-position: -3.6px 0;
    background-repeat: repeat-x;
  }
</style>
</head>
<body>
  <main class="label">
    <div class="label__frame"></div>

    <section class="label__front">
      <div class="flower-art" role="img" aria-label="Illustrazione botanica di un grappolo di fiori di acacia con foglie"></div>
      <h1 class="product-name">Acacia</h1>
      <p class="product-subtitle">MIELE ITALIANO DI ACACIA</p>
    </section>

    <div class="label__divider"></div>

    <section class="label__back">
      <div class="brand">
        <span class="brand__mark"></span>
        <span class="brand__name">PODERE OLMO</span>
      </div>

      <div class="fields">
        <div class="field">
          <p class="field__label">DA CONSUMARSI PREFERIBILMENTE ENTRO:</p>
          <div class="field__line"></div>
        </div>
        <div class="field">
          <p class="field__label">PRODOTTO DA AZIENDA AGRICOLA:</p>
          <div class="field__line"></div>
        </div>
        <div class="field">
          <p class="field__label">CONFEZIONATO PRESSO APICOLTURA:</p>
          <div class="field__line"></div>
        </div>
      </div>
    </section>
  </main>
</body>
</html>
```